Online trading school - Website design

We are building an online trading school (trading of shares, commodities, indices, currencies). The purpose is to teach online traders how to trade successfully. We need to design the homepage of the website and logo (bramwelloq.com will be the domain). The homepage will contain the following elements

- logo
- Sign in and Register links/buttons
- upper menu
- short introduction
- a couple of bullet points 'Why to join our school?'
- sign up form
- text
- bottom menu

Attached is a draft for the designer. The draft is just for an inspiration, the actual structure of the website can be different if the designer thinks so.

The designer is free to choose colors.

School

3 page

```html
<!DOCTYPE html>
<html lang="en">
<head>
<meta charset="utf-8">
<title>Bramwelloq – Online Trading School</title>
<link rel="stylesheet" href="https://fonts.googleapis.com/css2?family=Montserrat:wght@400;500&family=Open+Sans:wght@400;600&display=swap">
<style>
:root{
  --brand:#1b8fd0;
  --nav-top:#3bb2ee;
  --nav-bottom:#1790d8;
  --navy:#155f8f;
  --form-head:#0a86c6;
  --form-body:#1aa3e3;
  --ink:#333;
  --muted:#8a8a8a;
  --heading-grey:#555;
  --band:#f0f0f0;
  --footer:#0d3250;
  --white:#fff;
}
*{margin:0;padding:0;box-sizing:border-box}
html,body{width:1007px;height:1200px;overflow:hidden}
body{position:relative;font-family:'Open Sans',sans-serif;color:var(--ink);
  background:linear-gradient(180deg,#e3e5e8 0,#e9eaec 380px,#fff 480px,#fff 100%)}
.abs{position:absolute}
.logo{left:107px;top:40px;font-size:36px;font-weight:400;color:var(--brand);letter-spacing:-.5px;font-family:'Open Sans',sans-serif}
.social{left:601px;top:54px;display:flex;gap:6px}
.social span{width:28px;height:28px;border-radius:50%;background:var(--nav-bottom);border:2px solid #fff}
.btn-outline{top:52px;height:32px;border:2px solid var(--navy);font-family:'Montserrat',sans-serif;font-size:13px;font-weight:500;display:flex;align-items:center;justify-content:center;color:var(--navy)}
.btn-signin{left:710px;width:89px}
.btn-register{left:808px;width:89px;border-color:#2a9ed9;color:#2a9ed9}
.main-nav{left:106px;top:102px;width:791px;height:44px;display:flex;background:linear-gradient(var(--nav-top),var(--nav-bottom))}
.main-nav a{color:var(--white);text-decoration:none;font-family:'Montserrat',sans-serif;font-size:14px;font-weight:500;display:flex;align-items:center;justify-content:center;border-right:1px solid rgba(255,255,255,.45)}
.main-nav a:last-child{border:0}
.hero-panel{left:106px;top:150px;width:393px;height:288px;background:var(--navy);color:var(--white);padding:56px 0 0 41px}
.hero-panel h1{font-family:'Montserrat',sans-serif;font-weight:400;font-size:23px;margin-bottom:10px}
.hero-panel .lead{font-size:13.6px;line-height:21px;width:330px;margin-bottom:12px}
.hero-panel .body{font-size:11px;line-height:20.5px;width:330px}
.dots{display:flex;gap:3px;margin-top:13px}
.dots i{width:13px;height:13px;border-radius:50%;background:#fff;display:block}
.dots i:first-child{background:none;border:2px solid #fff}
.hero-photo{left:499px;top:150px;width:398px;height:288px;background:linear-gradient(135deg,#dfe7ef,#b9c9d8 45%,#c8a98a 75%,#e8e2da)}
.why{left:106px;top:476px;width:450px}
.why h2,.offer h2{font-family:'Montserrat',sans-serif;font-weight:400;font-size:28px}
.why h2{color:var(--brand);margin-bottom:8px}
.why p{font-size:11.6px;line-height:22px;color:var(--muted);padding-left:2px}
.benefits{list-style:none;margin-top:20px;padding-left:8px}
.benefits li{font-size:12.4px;height:29px;display:flex;align-items:flex-start;gap:10px}
.benefits svg{margin-top:3px}
.join{left:581px;top:471px;width:311px;height:279px;background:var(--form-body)}
.join h3{height:50px;background:var(--form-head);color:#fff;font-family:'Montserrat',sans-serif;font-weight:400;font-size:19px;padding:13px 0 0 28px}
.field{position:absolute;left:28px;width:259px;height:33px;background:#fff;font-size:12px;color:#8a8a8a;padding:9px 11px}
.agree{position:absolute;left:28px;top:196px;display:flex;align-items:center;gap:10px;color:#fff;font-size:12px}
.agree span{width:17px;height:16px;background:#fff;border-radius:2px}
.submit{position:absolute;left:27px;top:222px;width:260px;height:37px;background:var(--navy);color:#fff;font-family:'Montserrat',sans-serif;font-size:15px;font-weight:500;display:flex;align-items:center;justify-content:center}
.offer{left:0;top:796px;width:1007px;height:296px;background:var(--band);border-top:1px solid #dcdcdc;padding:57px 0 0 106px}
.offer h2{color:var(--heading-grey);margin-bottom:16px}
.offer p{font-size:11.6px;line-height:21.6px;color:var(--muted);width:790px;padding-left:3px;margin-bottom:10px}
.site-footer{left:0;top:1092px;width:1007px;height:108px;background:var(--footer);color:#fff}
.foot-nav{position:absolute;left:116px;top:25px;display:flex;gap:23px;font-size:13.6px}
.legal{position:absolute;right:106px;top:26px;text-align:right;font-size:11.6px;color:#c5d0da;line-height:23px}
.legal .links{margin-right:-3px}
</style>
</head>
<body>
<header>
  <div class="abs logo">Bramwelloq</div>
  <div class="abs social" aria-label="Social links"><span></span><span></span><span></span></div>
  <div class="abs btn-outline btn-signin">SIGN IN</div>
  <div class="abs btn-outline btn-register">REGISTER</div>
  <nav class="abs main-nav">
    <a style="width:207px">ABOUT OUR SCHOOL</a>
    <a style="width:149px">RISK WARNING</a>
    <a style="width:70px">FAQ</a>
    <a style="width:190px">TRADING GLOSSARY</a>
    <a style="width:175px;justify-content:flex-start;padding-left:20px">CONTACT</a>
  </nav>
</header>

<section class="abs hero-panel">
  <h1>Welcome to Our Website</h1>
  <p class="lead">Curabitur iaculis tempus eros Curabitur vel mi sit amet magna malesuada ultrices</p>
  <p class="body">et scelerisque mi tortor at ipsum cligula augue bibendum accumsan vestibulum ut commodo a mi Morbi ornare gravida elit Integer congue augue et malesuada iaculis</p>
  <div class="dots"><i></i><i></i><i></i><i></i></div>
</section>
<div class="abs hero-photo" role="img" aria-label="Photo of a teacher and students reviewing trading charts around a laptop"></div>

<section class="abs why">
  <h2>Why to Join Us?</h2>
  <p>Duis sed tellus et tortor vestibulum gravida Praesent elementum elit at tellus Curabitur metus ipsum luctus eu malesuada ut tincidunt sed diam</p>
  <ul class="benefits">
    <li><svg width="6" height="11"><path d="M0 0L6 5.5L0 11Z" fill="#1b3550"/></svg>Best Trading tips ever</li>
    <li><svg width="6" height="11"><path d="M0 0L6 5.5L0 11Z" fill="#1b3550"/></svg>Secret tips from experts</li>
    <li><svg width="6" height="11"><path d="M0 0L6 5.5L0 11Z" fill="#1b3550"/></svg>We teach you how to trade online</li>
    <li><svg width="6" height="11"><path d="M0 0L6 5.5L0 11Z" fill="#1b3550"/></svg>Learn how to trade commodities</li>
    <li><svg width="6" height="11"><path d="M0 0L6 5.5L0 11Z" fill="#1b3550"/></svg>Learn how to become a trader</li>
  </ul>
</section>

<section class="abs join">
  <h3>Join Our School Now!</h3>
  <div class="field" style="top:70px">First Name</div>
  <div class="field" style="top:112px">Last Name</div>
  <div class="field" style="top:153px">Email address</div>
  <div class="agree"><span></span>Agree with our terms and Conditions</div>
  <div class="submit">SUBMIT</div>
</section>

<section class="abs offer">
  <h2>What do We Offer?</h2>
  <p>Duis sed tellus et tortor vestibulum gravida Praesent elementum elit at tellus Curabitur metus ipsum luctus eu malesuada ut tincidunt sed diam Donec quis mi sed magna hendrerit accumsan Suspendisse risus nibh ultricies eu volutpat non condimentum</p>
  <p>Maecenas aliquet velit vel turpis Mauris neque metus malesuada nec ultricies sit amet porttitor mattis enim In massa libero interdum nec interdum vel blandit sed nulla In ullamcorper est eget tempor cursus neque mi consectetuer mi a ultricies massa est sed nisl Class aptent taciti sociosqu ad litora torquent per conubia nostra per inceptos hymenaeos</p>
</section>

<footer class="abs site-footer">
  <div class="foot-nav"><span>About Our School</span><span>Risk Warning</span><span>FAQ</span><span>Trading Glossary</span><span>Contact</span></div>
  <div class="legal">© 2016 Company Name&nbsp; All right reserved<br><span class="links">Term &amp; Conditions &nbsp;|&nbsp; Privacy Policy</span></div>
</footer>
</body>
</html>
```